Old Shanghai birthday party (1920s - 1930s)

I need an invitation for a joint birthday party; basically we will celebrate a couple: she's turning 40 and he's turning 45). The idea of the venue decoration is very sophisticate, with red lanterns, old style painted paper umbrellas and fans, check it out for your reference
https://www.tackboardly.com/rennavost/jazz-harbour/
Here the details to write down:
Marta and Dennis
are turning 85 !
Come celebrate with us!
Saturday, September 10th, 2016 at 8 pm
Quillberry
7C, 19 Tai Lok Fung Road, Aberdeen, Hong Kong
If you can come, please RSVP to Marta Felcote by August 20th
at (852) 471 26508
Dress code: Old Shanghai

Target Market(s)
Adults around 40 years old (The couple is from Australia)

```html
<!DOCTYPE html>
<html lang="en">
<head>
<meta charset="utf-8">
<title>Marta &amp; Dennis are turning 85 – Invitation</title>
<link rel="stylesheet" href="https://fonts.googleapis.com/css2?family=Archivo+Black&family=Yellowtail&family=Saira+Semi+Condensed:wght@300;400&display=swap">
<style>
  :root {
    --red-deep: #8e1416;
    --red-main: #d5262b;
    --red-bright: #e8403e;
    --band-dark: rgba(60, 8, 8, 0.55);
    --title-white: #ffffff;
    --script-gold: #f1dc9e;
    --detail-gold: #f6d9a0;
    --fan-pink: #e58aa8;
    --fan-green: #3c9a6a;
    --fan-orange: #eba450;
    --lantern-red: #b81d22;
  }
  * { margin: 0; padding: 0; box-sizing: border-box; }
  html, body { width: 846px; height: 1200px; overflow: hidden; background: #fff; }

  .invitation {
    position: relative;
    width: 846px;
    height: 1200px;
    overflow: hidden;
    background: var(--red-main);
  }

  .photo-fans {
    position: absolute;
    left: 0; top: 0;
    width: 345px; height: 1200px;
    background:
      linear-gradient(180deg,
        rgba(0,0,0,0) 0%,
        rgba(0,0,0,0) 60%,
        rgba(120,20,20,0.35) 100%),
      linear-gradient(160deg,
        var(--fan-green) 0%,
        var(--fan-pink) 18%,
        var(--fan-orange) 30%,
        var(--fan-pink) 42%,
        var(--fan-green) 55%,
        var(--fan-orange) 65%,
        var(--lantern-red) 80%,
        #6a3a2a 100%);
  }

  .photo-lanterns {
    position: absolute;
    left: 345px; top: 0;
    width: 501px; height: 1200px;
    background:
      radial-gradient(ellipse 70% 40% at 60% 15%, var(--red-bright) 0%, rgba(232,64,62,0) 70%),
      linear-gradient(180deg, var(--red-main) 0%, #c81f24 50%, var(--red-deep) 100%);
  }

  .footer-band {
    position: absolute;
    left: 0; top: 955px;
    width: 846px; height: 245px;
    background: var(--band-dark);
  }

  .headline {
    position: absolute;
    left: 0; top: 18px;
    width: 846px;
    text-align: center;
    font-family: "Archivo Black", "Arial Black", sans-serif;
    color: var(--title-white);
    font-size: 76px;
    line-height: 112px;
    letter-spacing: 1px;
    padding-left: 10px;
  }

  .tagline {
    position: absolute;
    left: 70px; top: 380px;
    width: 720px;
    font-family: "Yellowtail", cursive;
    color: var(--script-gold);
    font-size: 86px;
    line-height: 100px;
    transform: rotate(-21deg);
    transform-origin: left top;
    translate: 10px 170px;
  }
  .tagline-line { display: block; white-space: nowrap; }
  .tagline-line--second { padding-left: 150px; }

  .event-details,
  .rsvp {
    position: absolute;
    left: 345px;
    width: 501px;
    text-align: center;
    font-family: "Saira Semi Condensed", sans-serif;
    font-weight: 300;
    color: var(--detail-gold);
  }
  .event-details {
    top: 768px;
    font-size: 25px;
    line-height: 33px;
  }
  .rsvp {
    top: 1018px;
    font-size: 21px;
    line-height: 35px;
  }
  .dress-code { margin-top: 30px; }
</style>
</head>
<body>
  <main class="invitation">
    <div class="photo-fans" role="img" aria-label="Photo of colourful painted paper fans and red lanterns hanging among trees"></div>
    <div class="photo-lanterns" role="img" aria-label="Red-toned photo of a large red paper lantern with tassel"></div>
    <div class="footer-band"></div>

    <h1 class="headline">Marta &amp; Dennis<br>are turning 85 !</h1>

    <p class="tagline">
      <span class="tagline-line">Come celebrate</span>
      <span class="tagline-line tagline-line--second">with us!</span>
    </p>

    <section class="event-details">
      <p>Saturday, September 10th, 2016</p>
      <p>at 8 pm</p>
      <p>Quillberry</p>
      <p>7C, 19 Tai Lok Fung Road,</p>
      <p>Aberdeen, Hong Kong</p>
    </section>

    <section class="rsvp">
      <p>If you can come, please RSVP to</p>
      <p>Marta Felcote by August 20th</p>
      <p>at (852) 471 26508</p>
      <p class="dress-code">Dress Code : Old Shanghai</p>
    </section>
  </main>
</body>
</html>
```